Banner for homepage

It is a new banner for the homepage, temporary site address is 61.187.40.72 ( is the biggest banner only ) . Would be 5 variations for image content as below (in Portuguese ) :

Image 1:
Leitor de codigo de barras
Todos os tipos de leitores de código de barras para as mais diversas aplicações.
( example of product images in : http://www.quentorlabs.com/en-US/Pages/Category.aspx?category=barcode-scanners&cat=KLT)

Image 2:
Impressora de etiquetas
Identifique o que for nessário com o melhor custo/beneficio e flexibilidade de materiais de impressão.
( example of product images in : vintor.com in label printers desktop and industrial)

Image 3:
Impressora de cupom
Imprima recibos e cupons fiscais com agilidade e qualidade, temos a impressora certa para o seu PDV.
( example of product images in : http://www.palutrek.com.br/equipamento-categoria-impressoras+fiscais.html)

Image 4:
Coletor de dados
Computadores móveis com leitor de código de barras, que levam a automação para frente de trabalho.
( example of product images in : http://www.quentorlabs.com/en-US/Pages/Category.aspx?cat=KLT&category=hand-held-mobile-computer)

Image 5:
Etiquetas e Ribbons:
Etiquetas adesivas e não adesivas em vários de tipos de materiais, papéis e plásticos. O ribbon certo para impressão perfeita em cada material.
( example of product images in : http://www.tagmirelo.com/cats/supplies/barcode-printer.htm?nav=hdr)

```html
<!DOCTYPE html>
<html lang="pt-BR">
<head>
<meta charset="utf-8">
<title>Firmaline – Soluções em Automação e Código de barras</title>
<link rel="stylesheet" href="https://fonts.googleapis.com/css2?family=Oswald:wght@400;500;700&family=Jost:wght@400;500;600&family=Arimo:wght@400;700&display=swap">
<style>
  :root{
    --red:#cc353a;
    --white:#ffffff;
    --grey-text:#5a5a5a;
    --nav-top:#4a4a4a;
    --nav-bottom:#2e2e2e;
    --nav-text:#f0e2b0;
    --page:#ececec;
    --banner-bg:#d9d9db;
    --orange:#e8652a;
    --gold:#e2b56a;
    --brown-dark:#2f2a26;
    --taupe:#b3a49a;
  }
  *{box-sizing:border-box;margin:0;padding:0}
  html,body{width:1200px;height:588px;overflow:hidden}
  body{background:var(--page);font-family:"Arimo",Arial,sans-serif;position:relative}

  .site-header{position:absolute;left:0;top:0;width:1200px;height:107px;background:var(--red)}
  .brand{position:absolute;left:112px;top:14px;height:42px;display:flex;align-items:center}
  .brand-name{font-family:"Arimo",Arial,sans-serif;font-weight:700;font-size:30px;letter-spacing:3px;color:var(--white)}
  .brand-tagline{position:absolute;left:124px;top:62px;font-size:13px;color:var(--white)}

  .top-links{position:absolute;left:830px;top:11px;display:flex;font-size:12px;font-weight:700;color:var(--white)}
  .top-links span{padding:0 8px;border-left:1px solid rgba(255,255,255,.7);line-height:14px}
  .top-links span:first-child{border-left:0;padding-left:0}

  .contact-box{position:absolute;top:38px;height:47px;background:var(--white);padding:5px 10px;font-family:"Oswald",sans-serif}
  .contact-box .label{display:block;font-size:15px;color:#3a3a3a;line-height:18px}
  .contact-box .sub{display:block;font-size:11px;color:var(--orange);line-height:16px}
  .contact-chat{left:838px;width:113px}
  .contact-phone{left:967px;width:145px}
  .contact-phone svg{position:absolute;right:10px;top:19px}

  .main-nav{position:absolute;left:82px;top:97px;width:1052px;height:43px;background:linear-gradient(var(--nav-top),var(--nav-bottom));border-radius:3px;display:flex;align-items:center}
  .main-nav a{font-family:"Oswald",sans-serif;font-size:13px;color:var(--nav-text);text-decoration:none;padding:0 12px;height:43px;line-height:43px;border-right:1px solid #222;box-shadow:1px 0 0 #555;text-transform:uppercase;letter-spacing:-.2px}
  .search{position:absolute;right:10px;top:8px;width:150px;height:27px;background:#2a2a2a;border:1px solid #1a1a1a;border-radius:3px;font-size:12px;color:#bbb;padding:6px 6px}
  .search svg{position:absolute;right:6px;top:6px}

  .hero{position:absolute;left:104px;top:162px;width:749px;height:340px;background:var(--banner-bg);border:2px solid var(--white);border-radius:8px;box-shadow:0 2px 4px rgba(0,0,0,.1)}
  .hero-title{position:absolute;left:42px;top:32px;font-family:"Jost",sans-serif;font-weight:500;font-size:35px;line-height:38px;color:var(--red);letter-spacing:.5px}
  .hero-text{position:absolute;left:46px;top:120px;width:330px;font-family:"Jost",sans-serif;font-size:19px;line-height:23px;color:var(--grey-text)}
  .hero-button{position:absolute;left:42px;top:212px;width:156px;height:51px;border-radius:26px;background:var(--red);border:3px solid var(--white);color:var(--white);font-family:"Jost",sans-serif;font-size:20px;display:flex;align-items:center;justify-content:center;box-shadow:0 1px 3px rgba(0,0,0,.2)}
  .hero-product{position:absolute;left:420px;top:28px;width:285px;height:274px;border-radius:18px;background:linear-gradient(160deg,#5a5e5c,#333634)}

  .promo{position:absolute;left:879px;width:237px;height:163px;border-radius:3px;overflow:hidden}
  .promo-fast{top:162px;background:linear-gradient(135deg,#3d3631,var(--brown-dark))}
  .promo-invoice{top:340px;background:linear-gradient(135deg,#c2b4aa,var(--taupe))}
  .promo-title{position:absolute;left:24px;top:19px;font-family:"Oswald",sans-serif;font-weight:700;font-size:32px;line-height:36px;letter-spacing:-.5px}
  .promo-fast .promo-title{color:var(--gold)}
  .promo-invoice .promo-title{color:#3a3a3a}
  .promo-title .accent{color:var(--white)}
  .promo-text{position:absolute;left:24px;top:64px;font-size:12px;line-height:17px;color:var(--white);width:122px}
  .promo-art{position:absolute;right:10px;bottom:10px;width:95px;height:85px;border-radius:6px}
  .promo-fast .promo-art{background:linear-gradient(160deg,#d48a42,#8a4f20)}
  .promo-invoice .promo-art{background:linear-gradient(160deg,#1f5257,#0c2426)}
  .promo-button{position:absolute;left:22px;top:116px;width:94px;height:24px;border-radius:12px;font-family:"Oswald",sans-serif;font-size:12px;display:flex;align-items:center;justify-content:center}
  .promo-fast .promo-button{background:linear-gradient(#f0d2a0,#c99a55);color:#3b2a16}
  .promo-invoice .promo-button{background:linear-gradient(#e34a3c,#b3241e);color:var(--white)}

  .section-title{position:absolute;left:114px;top:536px;font-family:"Oswald",sans-serif;font-weight:500;font-size:19px;color:#3a3a3a}
  .section-band{position:absolute;left:104px;top:572px;width:1030px;height:16px;background:#dedede}
</style>
</head>
<body>
  <header class="site-header">
    <div class="brand"><span class="brand-name">FIRMALINE</span></div>
    <p class="brand-tagline">Soluções em Automação e Código de barras</p>
    <nav class="top-links"><span>Principal</span><span>Quem Somos</span><span>Entre em Contato</span></nav>
    <div class="contact-box contact-chat"><span class="label">CHAT ONLINE</span><span class="sub">CLIQUE AQUI</span></div>
    <div class="contact-box contact-phone"><span class="label">TELEFONES</span><span class="sub">TODOS OS ESTADOS</span>
      <svg width="8" height="5" viewBox="0 0 8 5"><path d="M0 0h8L4 5z" fill="#555"/></svg>
    </div>
  </header>

  <nav class="main-nav">
    <a>Leitor de código de barras</a>
    <a>Impressora de etiquetas</a>
    <a>Automação comercial</a>
    <a>Etiquetas</a>
    <a>Coletor de dados</a>
    <a>Impressora de cartão</a>
    <a>Marcas</a>
    <div class="search">Busca
      <svg width="12" height="12" viewBox="0 0 12 12"><circle cx="5" cy="5" r="3.5" fill="none" stroke="#ccc" stroke-width="1.6"/><path d="M7.6 7.6L11 11" stroke="#ccc" stroke-width="1.8"/></svg>
    </div>
  </nav>

  <section class="hero">
    <h1 class="hero-title">IMPRESSORA DE<br>CUPOM</h1>
    <p class="hero-text">Imprima recibos e cupons fiscais com agilidade e qualidade, temos a impressora certa para o seu PDV</p>
    <div class="hero-button">Veja Mais</div>
    <div class="hero-product" role="img" aria-label="Foto de uma impressora de cupom fiscal térmica cinza-escura"></div>
  </section>

  <aside class="promo promo-fast">
    <div class="promo-art" role="img" aria-label="Ilustração de uma caixa de papelão de entrega"></div>
    <h2 class="promo-title">Entrega<span class="accent">Rápida</span></h2>
    <p class="promo-text">Enviamos sua compra para todo o Brasil.</p>
    <div class="promo-button">Leia Mais</div>
  </aside>

  <aside class="promo promo-invoice">
    <div class="promo-art" role="img" aria-label="Ilustração de uma sacola de compras escura"></div>
    <h2 class="promo-title">Boleto<span class="accent">Faturado</span></h2>
    <p class="promo-text">Receba seu pedido com os boletos.</p>
    <div class="promo-button">Leia Mais</div>
  </aside>

  <h2 class="section-title">DESTAQUES</h2>
  <div class="section-band"></div>
</body>
</html>
```